Community Wellness FAIR 2023 Presenters

We need an image design that shows all of the presenters in our upcoming professional workshop. We will use this to promote in email newsletters, social media posts, and on our program website. The image should include the presenter's photo, full name with letters after their names, the FAIR logo, and the full program title. The details are listed below:

FAIR 2023 design Instructions

Program title:
Community Wellness Advisory & Venture FAIR 2023

Presenters Names:

Miranda Pollock Fairbairn, PhD, MPH - (should be positioned as the highlight, the leader, or main attraction)

Ronald Sutcliffe-Moor, MPH
Bethany Quarrington, MPH
Lorette Pemberly, PhD, MS, MPH
Greta Lindqvar, MPH
Tamira' Dobbs, MPH
Wallace Brisk, MPH
Dariel Fontaine, MS, MPH
Marisol Ochoa, MPH
Poppy Mercer, MS
Keisha Lomond, BS
Pavitra Ramalingaswamy, MPH
Talisha Cromby, DrPH, MS
Greta Vollmarin, MPH
Rosalind Tabbert, MPH

Brand colors:
#56588C
#F2E088
#F28444
#F24C27
#0D0D0D

```html
<!DOCTYPE html>
<html lang="en">
<head>
<meta charset="utf-8">
<title>Community Wellness Advisory &amp; Venture FAIR 2023 – Presenters</title>
<link rel="stylesheet" href="https://fonts.googleapis.com/css2?family=Poppins:wght@500;700;800;900&display=swap">
<style>
  :root{
    --indigo:#3b3a6b;
    --brand-purple:#56588C;
    --brand-orange:#F24C27;
    --brand-amber:#F28444;
    --ink:#0D0D0D;
    --paper:#ffffff;
    --photo-warm:#b88a70;
    --photo-cool:#9a9aa2;
  }
  *{box-sizing:border-box;margin:0;padding:0}
  html,body{width:1200px;height:1200px;overflow:hidden}
  body{background:var(--indigo);font-family:"Poppins",sans-serif;position:relative}
  .flyer{position:absolute;left:96px;top:42px;width:1008px;height:1116px;background:var(--paper);overflow:hidden}
  .brand{position:absolute;left:54px;top:62px;display:flex;align-items:center;gap:12px}
  .brand-dot{width:34px;height:34px;border-radius:50%;background:var(--brand-orange)}
  .brand-name{font-weight:700;font-size:30px;color:var(--brand-purple);line-height:1}
  .title{position:absolute;left:50px;top:170px;line-height:1}
  .title-main{display:block;font-weight:900;color:var(--brand-orange);font-size:76px;letter-spacing:-1.5px;line-height:100px}
  .title-sub{display:block;font-weight:800;color:var(--ink);font-size:42px;line-height:54px;margin-top:-4px}
  .title-year{display:block;font-weight:900;color:var(--brand-orange);font-size:84px;line-height:96px;margin-top:-4px}
  .feature{position:absolute;left:560px;top:14px;width:440px;height:580px}
  .feature svg{position:absolute;left:0;top:0}
  .feature-photo{position:absolute;left:70px;top:0;width:340px;height:527px;border-radius:170px 170px 0 0;background:linear-gradient(180deg,#3a2a22 0%,#6b4c3c 22%,#5a5d63 45%,#4a4d53 100%)}
  .feature-label{position:absolute;left:64px;top:527px;width:313px;height:44px;border-radius:6px;background:var(--brand-orange);color:#fff;font-weight:800;font-size:16px;line-height:19px;text-align:center;padding-top:3px;z-index:2}
  .presenter{position:absolute;width:200px;margin-left:-100px;text-align:center}
  .presenter-photo{width:116px;height:116px;margin:0 auto;border-radius:50%;border:4px solid var(--brand-orange);background:radial-gradient(circle at 50% 40%,var(--photo-warm) 0 32%,var(--photo-cool) 60%)}
  .presenter-name{margin-top:5px;color:var(--brand-orange);font-weight:800;font-size:14px;line-height:16.5px}
  .presenter-name.compact{font-size:11px;line-height:13px;margin-top:8px}
</style>
</head>
<body>
<main class="flyer">
  <div class="brand">
    <span class="brand-dot"></span>
    <span class="brand-name">Community Wellness FAIR</span>
  </div>

  <h1 class="title">
    <span class="title-main">COMMUNITY<br>WELLNESS</span>
    <span class="title-sub">ADVISORY &amp;<br>VENTURE</span>
    <span class="title-year">FAIR 2023</span>
  </h1>

  <section class="feature">
    <svg width="440" height="580" viewBox="0 0 440 580" aria-hidden="true">
      <path d="M218 533 C130 470 10 380 6 300 C2 250 40 238 100 238 C160 238 200 270 218 300 C236 270 280 238 340 238 C400 238 424 270 420 320 C414 410 300 480 218 533 Z" fill="var(--brand-orange)"/>
    </svg>
    <div class="feature-photo" role="img" aria-label="Portrait of lead presenter Miranda Pollock Fairbairn in a grey suit, arms crossed"></div>
    <div class="feature-label">Miranda Pollock Fairbairn<br>PhD, MPH</div>
  </section>

  <div class="presenter" style="left:135px;top:607px"><div class="presenter-photo" role="img" aria-label="Headshot of Ronald Sutcliffe-Moor"></div><p class="presenter-name">Ronald Sutcliffe-Moor<br>MPH</p></div>
  <div class="presenter" style="left:319px;top:607px"><div class="presenter-photo" role="img" aria-label="Headshot of Bethany Quarrington"></div><p class="presenter-name">Bethany Quarrington<br>MPH</p></div>
  <div class="presenter" style="left:505px;top:607px"><div class="presenter-photo" role="img" aria-label="Headshot of Lorette Pemberly"></div><p class="presenter-name">Lorette Pemberly<br>PhD, MS, MPH</p></div>
  <div class="presenter" style="left:685px;top:607px"><div class="presenter-photo" role="img" aria-label="Headshot of Greta Lindqvar"></div><p class="presenter-name">Greta Lindqvar<br>MPH</p></div>
  <div class="presenter" style="left:871px;top:607px"><div class="presenter-photo" role="img" aria-label="Headshot of Tamira' Dobbs"></div><p class="presenter-name">Tamira' Dobbs<br>MPH</p></div>

  <div class="presenter" style="left:135px;top:779px"><div class="presenter-photo" role="img" aria-label="Headshot of Wallace Brisk"></div><p class="presenter-name">Wallace Brisk<br>MPH</p></div>
  <div class="presenter" style="left:319px;top:779px"><div class="presenter-photo" role="img" aria-label="Headshot of Dariel Fontaine"></div><p class="presenter-name">Dariel Fontaine<br>MS, MPH</p></div>
  <div class="presenter" style="left:505px;top:779px"><div class="presenter-photo" role="img" aria-label="Headshot of Marisol Ochoa"></div><p class="presenter-name">Marisol Ochoa<br>MPH</p></div>
  <div class="presenter" style="left:685px;top:779px"><div class="presenter-photo" role="img" aria-label="Headshot of Poppy Mercer"></div><p class="presenter-name">Poppy Mercer<br>MS</p></div>
  <div class="presenter" style="left:871px;top:779px"><div class="presenter-photo" role="img" aria-label="Headshot of Keisha Lomond"></div><p class="presenter-name">Keisha Lomond<br>BS</p></div>

  <div class="presenter" style="left:225px;top:941px"><div class="presenter-photo" role="img" aria-label="Headshot of Pavitra Ramalingaswamy"></div><p class="presenter-name compact">Pavitra Ramalingaswamy<br>MPH</p></div>
  <div class="presenter" style="left:408px;top:941px"><div class="presenter-photo" role="img" aria-label="Headshot of Talisha Cromby"></div><p class="presenter-name">Talisha Cromby<br>DrPH, MS</p></div>
  <div class="presenter" style="left:594px;top:941px"><div class="presenter-photo" role="img" aria-label="Headshot of Greta Vollmarin"></div><p class="presenter-name">Greta Vollmarin<br>MPH</p></div>
  <div class="presenter" style="left:775px;top:941px"><div class="presenter-photo" role="img" aria-label="Black and white headshot of Rosalind Tabbert"></div><p class="presenter-name">Rosalind Tabbert<br>MPH</p></div>
</main>
</body>
</html>
```